Business Card Design Project

We need a business card design for an existing company that we have just acquired and need to refresh and revamp to give it a fresher, more modern, and professional image.
We are a niche high end management consulting firm working with large KVM400 type companies.
Our services include commercial advisory, change management, culture development, leadership and team development, and training.
The old website for this company is www.rvl-nqe.com.au that will give you a better understanding of what this business does.
However, we have updated the logo and are changing the website as well so your design for the business card might influence how we design the website.
Our corporate colours are red and white but we also use light grey, black, and dark blue (occasionally) on our stationery.
The final design should communicate partnership, creativity, performance, insight, and change.
Updates

Some of you were having trouble viewing the original logo file.  I have now updated another file with .jpg version of logo.  Hope this helps.

Target Market(s)

We are a consultancy firm servicing Top KVM or Zenith 300 type companies.

Industry/Entity Type

Management Consulting

Requirements
Must have
• Design must have all contact information and logo on 1 side of card. Back of card should be solid colour or watermarked only - i.e. no real writing on back of card.
Cards must be scannable by those new business card scanners that store the image electronically.
Will be printing on high quality paper with matte finish so design must be high definition to allow good printing.
Card must be normal business card size (no small or 3/4 sized cards).
Nice to have
• A design that has a bit of 'movement' in it rather than look blockish and rigid. Not sure how this can be done but something that gives the card a sense of flow because our work all about integrating and synthesising the 'hard' commercial aspects with the 'soft' human (psychological) dimensions into contracts and projects.
Design should be transferrable to stationery and website to the extent possible/sensible.
Should not have
• - 'old fashioned' or 'girly' or 'comical' fonts.

- no clip art like images

- no superfluous design features that convey no real message or idea.

```html
<!DOCTYPE html>
<html lang="en">
<head>
<meta charset="utf-8">
<title>KTR Group – Business Card</title>
<link rel="stylesheet" href="https://fonts.googleapis.com/css2?family=Source+Sans+3:wght@400;700&display=swap">
<style>
  :root {
    --backdrop: #6a7db6;
    --brand-red: #bc2029;
    --header-grey: #625d5b;
    --paper: #ffffff;
    --ink: #333333;
    --rule-grey: #8a8a8a;
    --ghost: rgba(255,255,255,0.2);
  }
  * { margin: 0; padding: 0; box-sizing: border-box; }
  html, body {
    width: 1024px; height: 1200px; overflow: hidden;
    background: var(--backdrop);
    font-family: "Source Sans 3", sans-serif;
    color: var(--ink);
  }
  .stage { position: relative; width: 1024px; height: 1200px; }

  .card-front {
    position: absolute; left: 75px; top: 57px;
    width: 875px; height: 499px;
    background: var(--paper); overflow: hidden;
  }
  .header-band {
    position: absolute; left: 0; top: 0; width: 100%; height: 124px;
    background: var(--header-grey);
  }
  .accent-band {
    position: absolute; left: 0; top: 131px; width: 100%; height: 19px;
    background: var(--brand-red);
  }
  .brand-mark {
    position: absolute; left: 73px; top: 48px;
    width: 192px; height: 194px;
    background: var(--brand-red);
    border: 3px solid var(--paper);
    outline: 1px solid var(--brand-red);
    display: flex; align-items: center; justify-content: center;
  }
  .brand-name {
    color: var(--paper); font-weight: 700; font-size: 34px;
    letter-spacing: 1px; text-align: center; line-height: 1;
  }
  .person {
    position: absolute; left: 302px; top: 65px;
    font-size: 23.5px; color: var(--paper); white-space: nowrap;
  }
  .person-name { font-weight: 700; }
  .person-divider {
    display: inline-block; width: 1.5px; height: 27px;
    background: var(--paper); vertical-align: -5px; margin: 0 9px;
  }
  .tagline {
    position: absolute; left: 40px; top: 249px; font-size: 23px; white-space: nowrap;
  }
  .phones {
    position: absolute; right: 40px; top: 196px;
    text-align: right; font-size: 23px; line-height: 30px; white-space: nowrap;
  }
  .label { font-weight: 700; }
  .address {
    position: absolute; left: 35px; top: 386px;
    font-size: 22px; line-height: 36px; font-style: normal; white-space: nowrap;
  }
  .info-divider {
    position: absolute; left: 415px; top: 375px;
    width: 2px; height: 87px; background: var(--rule-grey);
  }
  .online {
    position: absolute; left: 446px; top: 383px;
    font-size: 22px; line-height: 36px; white-space: nowrap;
  }

  .card-back {
    position: absolute; left: 69px; top: 622px;
    width: 875px; height: 499px;
    background: var(--brand-red);
  }
  .back-mark {
    position: absolute; left: 295px; top: 101px;
    width: 300px; height: 301px;
    border: 2px solid var(--ghost);
  }
  .back-mark-frame {
    position: absolute; inset: 12px;
    border: 2px solid var(--ghost);
    display: flex; align-items: center; justify-content: center;
  }
  .back-mark-name {
    color: var(--ghost); font-weight: 700; font-size: 46px;
    letter-spacing: 2px; white-space: nowrap;
  }
</style>
</head>
<body>
<main class="stage">
  <section class="card-front" aria-label="Business card front">
    <div class="header-band"></div>
    <div class="accent-band"></div>
    <div class="brand-mark"><span class="brand-name">KTR<br>GROUP</span></div>
    <p class="person"><span class="person-name">Tom Harwick</span><span class="person-divider"></span>Partner - Head of Advisory Services</p>
    <p class="tagline">Know - Transform - Realise</p>
    <div class="phones">
      <p><span class="label">Mobile :</span> +61 (0)400 555 018</p>
      <p><span class="label">Fax :</span> +61 3 9000 1270</p>
      <p><span class="label">Tel :</span> +61 3 9000 1274</p>
    </div>
    <address class="address">
      Level 6, 120 Harbour St, Melbourne,<br>Vic 3000, Australia
    </address>
    <div class="info-divider"></div>
    <div class="online">
      <p><span class="label">Email :</span> tom.harwick@ktrgroup.com.au</p>
      <p><span class="label">Web :</span> www.ktrgroup.com.au</p>
    </div>
  </section>

  <section class="card-back" aria-label="Business card back">
    <div class="back-mark">
      <div class="back-mark-frame"><span class="back-mark-name">KTR GROUP</span></div>
    </div>
  </section>
</main>
</body>
</html>
```